Website Design - Financial Services Software

We are looking for website designs for our public website.
Some competitor sites we like are
www.torvani.com.au
www.pluma.com.au
www.quentabridge.com
www.morlupa.com.au

A wireframe example of our site can be found at
http://pr4tqz.bivlowpage.com/

Attached is our logo.

Industry/Entity Type

Financial

```html
<!DOCTYPE html>
<html lang="en">
<head>
<meta charset="utf-8">
<title>Velluma – Smarter Financial Strategies</title>
<link rel="stylesheet" href="https://fonts.googleapis.com/css2?family=Open+Sans:wght@400;600;700&display=swap">
<style>
  :root {
    --navy: #0b2d5e;
    --hero-blue: #4a6b8e;
    --cta-blue: #1f64b0;
    --pill-grey: #a9a9a9;
    --panel-grey: #f4f4f4;
    --panel-border: #cccccc;
    --text-dark: #222222;
    --text-muted: #8a8a8a;
    --link-muted: #9a9a9a;
    --white: #ffffff;
  }
  * { box-sizing: border-box; margin: 0; padding: 0; }
  html, body { width: 1022px; height: 1200px; overflow: hidden; }
  body {
    position: relative;
    background: var(--white);
    font-family: "Open Sans", Arial, sans-serif;
    color: var(--text-dark);
    border-top: 2px solid var(--navy);
  }
  .abs { position: absolute; }

  /* Brand */
  .brand { display: flex; flex-direction: column; align-items: center; }
  .brand-mark { width: 44px; height: 44px; border-radius: 50%; background: var(--text-dark); margin-bottom: 10px; }
  .brand-name { font-size: 28px; font-weight: 600; letter-spacing: 1px; line-height: 1; color: var(--text-dark); }
  .brand-tag { font-size: 8px; font-weight: 600; letter-spacing: .4px; margin-top: 3px; color: var(--text-dark); }
  .site-brand { left: 86px; top: 14px; width: 140px; }
  .footer-brand { left: 82px; top: 976px; width: 140px; }

  /* Header */
  .login-btn {
    left: 841px; top: 36px; width: 96px; height: 25px;
    background: var(--navy); color: var(--white);
    font-size: 12px; font-weight: 600;
    display: flex; align-items: center; justify-content: center;
  }
  .nav-pill {
    top: 97px; height: 29px; border-radius: 15px;
    background: var(--pill-grey); color: var(--white);
    font-size: 12px; font-weight: 600;
    display: flex; align-items: center; justify-content: center;
  }
  .nav-pill.is-active { background: var(--navy); }

  /* Hero */
  .hero { left: 86px; top: 139px; width: 851px; height: 370px; background: var(--hero-blue); }
  .hero-title { left: 30px; top: 70px; font-size: 25px; font-weight: 600; color: var(--white); }
  .hero-sub { left: 30px; top: 118px; width: 350px; font-size: 17px; font-weight: 600; line-height: 25px; color: var(--white); }
  .tour-card { top: 206px; width: 164px; }
  .tour-photo { position: relative; height: 91px; }
  .tour-label {
    position: absolute; left: 0; right: 0; bottom: 0; height: 25px;
    background: rgba(0,0,0,.55); color: var(--white);
    font-size: 12px; font-weight: 600;
    display: flex; align-items: center; justify-content: center;
  }
  .tour-link { margin-top: 8px; text-align: center; font-size: 13px; font-weight: 600; color: var(--white); }
  .video { left: 411px; top: 30px; width: 410px; height: 311px; background: linear-gradient(160deg, #dcdcdc 0%, #b8b8b4 45%, #8f918a 100%); }
  .video-play { position: absolute; left: 190px; top: 123px; width: 40px; height: 40px; }
  .video-caption { position: absolute; left: 39px; color: var(--white); font-weight: 600; display: flex; align-items: center; padding-left: 18px; }
  .video-caption.primary { top: 214px; width: 232px; height: 30px; background: var(--navy); font-size: 14px; }
  .video-caption.secondary { top: 258px; width: 94px; height: 25px; background: #252525; font-size: 14px; padding-left: 16px; }

  /* Intro panel */
  .intro { left: 86px; top: 539px; width: 851px; height: 232px; background: var(--panel-grey); border: 1px solid var(--panel-border); }
  .intro-title { left: 20px; top: 16px; font-size: 14px; font-weight: 600; color: #555; }
  .intro-copy { left: 20px; top: 56px; width: 331px; font-size: 10.5px; line-height: 16px; color: var(--text-muted); text-align: justify; }
  .intro-copy p + p { margin-top: 16px; }
  .gallery-tile { width: 141px; height: 81px; }

  /* CTA */
  .cta { left: 86px; top: 804px; width: 851px; height: 88px; background: var(--navy); }
  .cta-text { left: 29px; top: 28px; font-size: 21px; font-weight: 600; color: var(--white); }
  .cta-btn {
    left: 585px; top: 23px; width: 245px; height: 38px; background: var(--cta-blue);
    color: var(--white); font-size: 15px; font-weight: 700;
    display: flex; align-items: center; justify-content: center;
  }

  /* Footer */
  .footer-heading { font-size: 13px; font-weight: 600; color: var(--text-dark); }
  .footer-links { list-style: none; font-size: 11px; line-height: 21.5px; color: var(--link-muted); }
  .footer-links .is-current { color: #2c2f7a; }
  .social-tile { left: 879px; width: 25px; height: 25px; background: #cfcfcf; border-radius: 2px; }
  .legal-bar {
    left: 0; top: 1146px; width: 1022px; height: 54px; background: var(--navy);
    color: var(--white); font-size: 11px;
    display: flex; align-items: center; justify-content: center; gap: 7px;
  }
</style>
</head>
<body>

  <header>
    <div class="abs brand site-brand">
      <span class="brand-mark"></span>
      <span class="brand-name">VELLUMA</span>
      <span class="brand-tag">SMARTER FINANCIAL STRATEGIES</span>
    </div>
    <div class="abs login-btn">LOGIN</div>
    <nav>
      <div class="abs nav-pill is-active" style="left:469px;width:125px;">FEATURES</div>
      <div class="abs nav-pill" style="left:607px;width:124px;">EXAMPLES</div>
      <div class="abs nav-pill" style="left:745px;width:89px;">FAQ</div>
      <div class="abs nav-pill" style="left:847px;width:89px;">ABOUT</div>
    </nav>
  </header>

  <section class="abs hero">
    <h1 class="abs hero-title">Smarter Financial Strategies</h1>
    <p class="abs hero-sub">Values and Cash-flow focused financial software for financial planners</p>

    <div class="abs tour-card" style="left:31px;">
      <div class="tour-photo" role="img" aria-label="Photo of a smiling couple outdoors" style="background:linear-gradient(135deg,#6f5a4a,#c9a489 55%,#8a7a6a);">
        <span class="tour-label">For planning Practices</span>
      </div>
      <div class="tour-link">Feature Tour</div>
    </div>
    <div class="abs tour-card" style="left:210px;">
      <div class="tour-photo" role="img" aria-label="Silhouettes of two businessmen shaking hands over puzzle pieces" style="background:linear-gradient(180deg,#dbe9f2 0%,#9fcbe6 45%,#6aa84f 70%,#2f7fbf 100%);">
        <span class="tour-label">For Dealer Groups</span>
      </div>
      <div class="tour-link">Feature Tour</div>
    </div>

    <div class="abs video" role="img" aria-label="Video still of banknotes in a glass jar labelled Finance">
      <svg class="video-play" viewBox="0 0 40 40">
        <circle cx="20" cy="20" r="20" fill="#d0202a"/>
        <path d="M16 13 L28 20 L16 27 Z" fill="#ffffff"/>
      </svg>
      <div class="video-caption primary">Smarter Financial Strategies</div>
      <div class="video-caption secondary">Velluma</div>
    </div>
  </section>

  <section class="abs intro">
    <h2 class="abs intro-title">Lorem Ipsum</h2>
    <div class="abs intro-copy">
      <p>Simply dummy text of the printing and typesetting industry. Lorem Ipsum has been the industry's standard dummy text ever since the 1500s, when an unknown printer took a galley of type and scrambled it to make a type specimen book. It has survived not only five centuries, but also the leap</p>
      <p>into electronic typesetting, remaining essentially unchanged. It was popularised in the 1960s with the release of Letraset sheets containing.</p>
    </div>
    <div class="abs gallery-tile" role="img" aria-label="Business team working at laptops" style="left:381px;top:28px;background:linear-gradient(135deg,#d9dde2,#4a4f5a);"></div>
    <div class="abs gallery-tile" role="img" aria-label="Businessman seated at a desk by a harbour window" style="left:535px;top:28px;background:linear-gradient(180deg,#8fb6c4,#3d5f6c 60%,#1f2a30);"></div>
    <div class="abs gallery-tile" role="img" aria-label="Office workers at computer screens" style="left:689px;top:28px;background:linear-gradient(135deg,#6b6b6b,#c9c4bc 50%,#3d3d3d);"></div>
    <div class="abs gallery-tile" role="img" aria-label="Hand drawing a rising line chart" style="left:381px;top:121px;background:linear-gradient(135deg,#cfc8c2,#f7f7f7 60%,#ffffff);"></div>
    <div class="abs gallery-tile" role="img" aria-label="Businesswoman in front of a red bus" style="left:535px;top:121px;background:linear-gradient(135deg,#c8202a,#e9e0d6 55%,#2a2a2a);"></div>
    <div class="abs gallery-tile" role="img" aria-label="Woman standing in an autumn street" style="left:689px;top:121px;background:linear-gradient(135deg,#d9a04a,#b06a2a 50%,#4a3a2a);"></div>
  </section>

  <section class="abs cta">
    <p class="abs cta-text">Create an Account today and begin your 30 day trail!</p>
    <div class="abs cta-btn">SIGN UP NOW!</div>
  </section>

  <footer>
    <div class="abs brand footer-brand">
      <span class="brand-mark"></span>
      <span class="brand-name">VELLUMA</span>
      <span class="brand-tag">SMARTER FINANCIAL STRATEGIES</span>
    </div>

    <div class="abs" style="left:298px;top:977px;">
      <h3 class="footer-heading">ABOUT</h3>
      <ul class="footer-links" style="margin-top:14px;">
        <li class="is-current">ABOUT US</li>
        <li>SUCCESS STORIES</li>
        <li>BECOMING A SOLUTION PARTNER</li>
      </ul>
    </div>
    <div class="abs" style="left:523px;top:977px;">
      <h3 class="footer-heading">GETING STARTED</h3>
      <ul class="footer-links" style="margin-top:14px;">
        <li>DOCUMENTATION</li>
        <li>KNOWLEDGE-BASE</li>
        <li>PREMIUM SUPPORT</li>
      </ul>
    </div>
    <div class="abs" style="left:703px;top:977px;">
      <h3 class="footer-heading">LEGAL</h3>
      <ul class="footer-links" style="margin-top:14px;">
        <li>DOCUMENTATION</li>
        <li>KNOWLEDGE-BASE</li>
        <li>PREMIUM SUPPORT</li>
      </ul>
    </div>
    <h3 class="abs footer-heading" style="left:878px;top:972px;">CONNECT</h3>
    <div class="abs social-tile" style="top:1013px;" aria-label="Social profile"></div>
    <div class="abs social-tile" style="top:1046px;" aria-label="Social profile"></div>

    <div class="abs legal-bar">
      <span>Copyright © yourwebsite</span><span>|</span>
      <span>Terms &amp; Conditions</span><span>|</span>
      <span>Privacy Policy</span><span>|</span>
      <span>Cookies Policy</span><span>|</span>
      <span>Contact us</span>
    </div>
  </footer>

</body>
</html>
```